Wine label design for my wife. Wine called "The Mirabel"

I need a wine label face lift of one of my premium wines in my collection. My wine sells in Harbor Lark's all over the States. My current label is called The Mirabel (my wife's name) and the illustration of her eyes is done by a well know artist from South Africa. I do not have to use this illustration and therefor I attached several pictures of her and her eyes, even when she was a little girl. The wine's also made in South Africa. This is a premium wine that we only sell 2000 bottles per year. The wine sells at 60 usd per bottle, The current label is too white. I also think her eyes should look more at the person buying it, than away from them.

Target Market(s)

Top end wine buyers

Font styles to use
Decorative
Script

Requirements
Must have
• 'The Mirabel' must be on the label
An illustration must be on the label
Basically all the info that's on the current label must be on by law. As per Sample
Nice to have
• Maybe some ideas of her whole face?
Should not have
• any gold colour

```html
<!DOCTYPE html>
<html lang="en">
<head>
<meta charset="utf-8">
<title>The Mirabel – Sauvignon Blanc Label</title>
<link rel="stylesheet" href="https://fonts.googleapis.com/css2?family=Great+Vibes&family=Tinos&display=swap">
<style>
  :root {
    --backdrop: #b3bcbb;
    --paper: #f7f4ee;
    --paper-edge: #e4dfd5;
    --wine-red: #a8243a;
    --ink: #2a2624;
    --portrait-light: #e6ddd7;
    --portrait-mid: #b7aca6;
    --portrait-dark: #5d5551;
    --ornament: #8a6a5a;
  }
  * { margin: 0; padding: 0; box-sizing: border-box; }
  html, body {
    width: 1003px;
    height: 1200px;
    overflow: hidden;
    background: var(--backdrop);
  }
  .canvas {
    position: relative;
    width: 1003px;
    height: 1200px;
  }
  .label {
    position: absolute;
    left: 48px;
    top: 105px;
    width: 908px;
    height: 990px;
    background: var(--paper);
    box-shadow: inset 0 0 28px var(--paper-edge);
    clip-path: polygon(
      0% 1%, 6% 0%, 14% 0.8%, 25% 0%, 38% 0.6%, 52% 0%, 66% 0.9%, 79% 0%, 90% 0.7%, 100% 0%,
      99.2% 10%, 100% 22%, 99.4% 36%, 100% 50%, 99.3% 63%, 100% 77%, 99.5% 89%, 100% 100%,
      88% 99.2%, 75% 100%, 61% 99.4%, 47% 100%, 33% 99.3%, 20% 100%, 8% 99.4%, 0% 100%,
      0.7% 88%, 0% 74%, 0.6% 60%, 0% 46%, 0.8% 32%, 0% 18%
    );
  }
  .corner-ornament {
    position: absolute;
    top: 26px;
    width: 130px;
    height: 90px;
    background: radial-gradient(ellipse at center, rgba(138,106,90,0.28), rgba(138,106,90,0) 70%);
  }
  .corner-ornament--left { left: 26px; }
  .corner-ornament--right { right: 26px; }
  .wine-name {
    position: absolute;
    top: 40px;
    left: 0;
    width: 100%;
    text-align: center;
    font-family: "Great Vibes", cursive;
    font-size: 126px;
    line-height: 1;
    color: var(--wine-red);
  }
  .varietal {
    position: absolute;
    top: 226px;
    left: 0;
    width: 100%;
    text-align: center;
    font-family: "Tinos", serif;
    font-size: 58px;
    line-height: 1;
    color: var(--ink);
    letter-spacing: 1px;
  }
  .portrait {
    position: absolute;
    left: 47px;
    top: 302px;
    width: 797px;
    height: 344px;
    background:
      linear-gradient(90deg, var(--portrait-dark) 0%, var(--portrait-mid) 7%, var(--portrait-light) 22%, var(--portrait-light) 78%, var(--portrait-mid) 92%, var(--portrait-dark) 100%);
  }
  .producer {
    position: absolute;
    top: 722px;
    left: 0;
    width: 100%;
    text-align: center;
    font-family: "Tinos", serif;
    font-size: 56px;
    line-height: 1;
    color: var(--ink);
  }
  .vintage {
    position: absolute;
    top: 800px;
    left: 0;
    width: 100%;
    text-align: center;
    font-family: "Tinos", serif;
    font-size: 66px;
    line-height: 1;
    color: var(--ink);
  }
  .scroll-ornament {
    position: absolute;
    left: 84px;
    top: 880px;
    width: 740px;
    height: 56px;
    background: radial-gradient(ellipse at center, rgba(42,38,36,0.22), rgba(42,38,36,0) 70%);
  }
</style>
</head>
<body>
  <main class="canvas">
    <section class="label">
      <div class="corner-ornament corner-ornament--left" role="img" aria-label="Decorative corner flourish"></div>
      <div class="corner-ornament corner-ornament--right" role="img" aria-label="Decorative corner flourish"></div>
      <h1 class="wine-name">The Mirabel</h1>
      <p class="varietal">SAUVIGNON BLANC</p>
      <div class="portrait" role="img" aria-label="Black and white illustration of a woman's eyes and brows"></div>
      <p class="producer">HOLLIS CRANE WINES</p>
      <p class="vintage">2017</p>
      <div class="scroll-ornament" role="img" aria-label="Decorative scroll flourish"></div>
    </section>
  </main>
</body>
</html>
```